Talvo shoes is a wholesale shoe sales company , mostly working in female shoes and kiddies shoes with a small mens section . looking for a clean slick look. http://www.kemrafootwear.co.za/shop/ is a good reference

It Company

```html
<!DOCTYPE html>
<html lang="en">
<head>
<meta charset="utf-8">
<title>Talvo Shoes</title>
<link href="https://fonts.googleapis.com/css2?family=Open+Sans:ital,wght@0,400;0,600;0,700;0,800;1,800&family=Ubuntu:wght@400;500&display=swap" rel="stylesheet">
<style>
:root{
  --ink:#333333;
  --header:#353535;
  --white:#ffffff;
  --accent:#e8483a;
  --accent-soft:rgba(222,52,70,.72);
  --signup:#e0143c;
  --ribbon:#1e9be6;
  --muted:#555555;
  --rule:#cfcfcf;
  --bag:#f5c400;
}
*{box-sizing:border-box;margin:0;padding:0}
html,body{width:1024px;height:1200px;overflow:hidden;background:var(--white)}
body{position:relative;font-family:"Open Sans",Arial,sans-serif;color:var(--ink)}
.site-header{position:absolute;left:0;top:0;width:1024px;height:98px;background:var(--header)}
.brand{position:absolute;left:18px;top:32px;display:flex;align-items:center;gap:8px;color:var(--white);font-weight:700;font-size:29px;letter-spacing:.2px}
.brand-dot{width:16px;height:16px;border-radius:50%;background:var(--white)}
.account-tab{position:absolute;left:850px;top:2px;width:117px;height:23px;background:var(--white);font-size:11px;font-weight:600;text-align:center;line-height:23px}
.promo{position:absolute;left:325px;top:58px;color:var(--white);font-size:13.5px;letter-spacing:.2px}
.promo b{font-weight:700}
.search{position:absolute;left:627px;top:55px;width:230px;height:24px;background:var(--white);border:1px solid #bbb}
.search span{position:absolute;left:8px;top:4px;font-size:10px;color:#444}
.search i{position:absolute;right:0;top:0;width:26px;height:22px;border-left:1px solid #bbb}
.bag{position:absolute;left:860px;top:44px;width:100px;text-align:right;color:var(--white)}
.bag-title{font-size:17px;font-family:"Ubuntu",sans-serif}
.bag-total{font-size:10.5px;font-weight:600}
.bag-icon{position:absolute;left:966px;top:44px}
.main-nav{position:absolute;left:0;top:98px;width:1024px;height:40px;display:flex;font-family:"Ubuntu",sans-serif;font-size:14px;color:#3a3a3a}
.main-nav a{position:absolute;top:12px;color:inherit;text-decoration:none}
.tile{position:absolute;overflow:hidden}
.tile-label{position:absolute;width:103px;height:103px;border-radius:50%;background:var(--accent-soft);color:var(--white);font-weight:700;font-size:13px;display:flex;align-items:center;justify-content:center;letter-spacing:.2px}
.product{position:absolute;top:672px;width:160px}
.product-shot{width:150px;height:155px;border-radius:4px}
.price{position:absolute;top:190px;left:0;font-size:15px;font-weight:700;white-space:nowrap}
.note{position:absolute;top:210px;left:0;font-size:11px;white-space:nowrap;letter-spacing:.3px}
.add-btn{position:absolute;top:225px;left:-2px;width:72px;height:21px;background:var(--accent);color:var(--white);font-weight:700;font-size:13px;display:flex;align-items:center;gap:8px;padding-left:7px}
.newsletter{position:absolute;left:48px;top:982px;width:911px;height:112px;background:linear-gradient(90deg,#fafafa,#e8e8e8);overflow:hidden}
.ribbon{position:absolute;left:43px;top:977px}
.nl-title{position:absolute;left:42px;top:22px;font-size:23px;font-weight:800;font-style:italic;color:#555}
.nl-copy{position:absolute;left:41px;top:56px;width:190px;font-size:10.5px;line-height:16px;letter-spacing:.2px}
.nl-input{position:absolute;left:242px;top:55px;width:242px;height:30px;border:1px solid #888;background:var(--white);font-size:13px;color:#666;padding:5px 9px}
.nl-btn{position:absolute;left:487px;top:55px;width:88px;height:30px;background:var(--signup);color:var(--white);font-weight:700;font-size:12.5px;text-align:center;line-height:30px}
.nl-photos{position:absolute;left:562px;top:0;height:112px;width:349px}
.footer-rule{position:absolute;left:0;top:1130px;width:1024px;height:1px;background:var(--rule)}
.footer-links{position:absolute;left:21px;top:1149px;display:flex;gap:20px;font-size:12px}
.footer-links a{color:var(--ink);text-decoration:underline}
.copyright{position:absolute;left:21px;top:1171px;font-size:12px}
.pay{position:absolute;top:1149px;height:20px;border-radius:2px}
</style>
</head>
<body>
<header class="site-header">
  <div class="brand"><span class="brand-dot"></span>TALVO SHOES</div>
  <div class="account-tab">Login | Register</div>
  <div class="promo">DELIVERY AND RETURNS <b>ARE ALWAYS FREE</b></div>
  <div class="search"><span>Search</span><i></i></div>
  <div class="bag"><div class="bag-title">MyBag</div><div class="bag-total">0 item(s) - $0.00</div></div>
  <svg class="bag-icon" width="28" height="42" viewBox="0 0 28 42" aria-hidden="true"><path d="M9 10 V5 a5 5 0 0 1 10 0 V10" fill="none" stroke="#f5c400" stroke-width="2"/><rect x="1" y="9" width="26" height="24" fill="var(--bag)"/><rect x="1" y="33" width="26" height="8" fill="#f5c400" opacity=".25"/></svg>
</header>

<nav class="main-nav">
  <a style="left:100px">Ladies</a><a style="left:180px">Mens</a><a style="left:253px">Girls</a><a style="left:322px">Boys</a><a style="left:397px">Accessories</a><a style="left:507px">Events</a><a style="left:589px">About Talvo</a><a style="left:705px">Stores</a><a style="left:784px">Faq's</a><a style="left:856px">Contact Us</a>
</nav>

<div class="tile" style="left:58px;top:139px;width:449px;height:336px;background:linear-gradient(135deg,#e6e6e6,#b8ad95 60%,#2a2a2a)" role="img" aria-label="Woman in black sequin dress fastening strappy heels">
  <div class="tile-label" style="left:173px;top:116px">WOMEN</div></div>
<div class="tile" style="left:517px;top:139px;width:450px;height:336px;background:linear-gradient(90deg,#c4ad8a,#e0d8c8 45%,#4a5f80 70%,#8a6a4a)" role="img" aria-label="Two men seated in chinos wearing leather brogues">
  <div class="tile-label" style="left:173px;top:116px">MEN</div></div>
<div class="tile" style="left:58px;top:484px;width:297px;height:164px;background:linear-gradient(90deg,#d0c8cc,#c94a5a 60%,#e28a40)" role="img" aria-label="Silver glitter platform heel">
  <div class="tile-label" style="left:97px;top:30px">GIRLS</div></div>
<div class="tile" style="left:363px;top:484px;width:297px;height:164px;background:linear-gradient(180deg,#6d7a8a,#6a7a40 60%,#5a5040)" role="img" aria-label="Kids in jeans and sneakers sitting on a log">
  <div class="tile-label" style="left:97px;top:30px">BOYS</div></div>
<div class="tile" style="left:668px;top:484px;width:298px;height:164px;background:linear-gradient(90deg,#e0dcd8,#e8552e 45%,#d0c8c0)" role="img" aria-label="Orange leather handbag">
  <div class="tile-label" style="left:97px;top:30px">ACCESSORIES</div></div>

<div class="product" style="left:96px"><div class="product-shot" style="margin-left:-14px;background:radial-gradient(#d8c4a8,#fff 70%)" role="img" aria-label="Gold studded platform pump"></div><div class="price">$120.00</div><div class="note">available in more colors</div><div class="add-btn"><svg width="12" height="12" viewBox="0 0 12 12"><rect x="1" y="4" width="10" height="8" fill="#fff"/><path d="M4 4V2.5a2 2 0 0 1 4 0V4" stroke="#fff" fill="none"/></svg>ADD</div></div>
<div class="product" style="left:279px"><div class="product-shot" style="margin-left:-10px;background:radial-gradient(#222,#fff 70%)" role="img" aria-label="Black patent peep-toe stiletto"></div><div class="price">$120.00</div><div class="note">available in more colors</div><div class="add-btn"><svg width="12" height="12" viewBox="0 0 12 12"><rect x="1" y="4" width="10" height="8" fill="#fff"/><path d="M4 4V2.5a2 2 0 0 1 4 0V4" stroke="#fff" fill="none"/></svg>ADD</div></div>
<div class="product" style="left:457px"><div class="product-shot" style="margin-left:-10px;background:radial-gradient(#1a1a1a,#fff 70%)" role="img" aria-label="Black patent cross-strap pumps"></div><div class="price">$120.00</div><div class="note">available in more colors</div><div class="add-btn"><svg width="12" height="12" viewBox="0 0 12 12"><rect x="1" y="4" width="10" height="8" fill="#fff"/><path d="M4 4V2.5a2 2 0 0 1 4 0V4" stroke="#fff" fill="none"/></svg>ADD</div></div>
<div class="product" style="left:642px"><div class="product-shot" style="margin-left:-8px;background:radial-gradient(#6a4a38,#fff 70%)" role="img" aria-label="Brown suede fur-cuff boot"></div><div class="price">$120.00</div><div class="note">available in more colors</div><div class="add-btn"><svg width="12" height="12" viewBox="0 0 12 12"><rect x="1" y="4" width="10" height="8" fill="#fff"/><path d="M4 4V2.5a2 2 0 0 1 4 0V4" stroke="#fff" fill="none"/></svg>ADD</div></div>
<div class="product" style="left:810px"><div class="product-shot" style="margin-left:-10px;background:radial-gradient(#7a2a38,#fff 70%)" role="img" aria-label="Burgundy leather ankle bootie"></div><div class="price">$120.00</div><div class="note">available in more colors</div><div class="add-btn"><svg width="12" height="12" viewBox="0 0 12 12"><rect x="1" y="4" width="10" height="8" fill="#fff"/><path d="M4 4V2.5a2 2 0 0 1 4 0V4" stroke="#fff" fill="none"/></svg>ADD</div></div>

<section class="newsletter">
  <div class="nl-title">Newsletter</div>
  <p class="nl-copy">Email Newsletter Join our email list to get exclusive info and enter our monthly shoe giveaway.</p>
  <div class="nl-input">Email address</div>
  <div class="nl-btn">SIGN UP</div>
  <svg class="nl-photos" viewBox="0 0 349 112" role="img" aria-label="Three photos of lace-up ankle boots">
    <defs>
      <linearGradient id="bootA" x1="0" y1="0" x2="0" y2="1"><stop offset="0" stop-color="#c8c4c0"/><stop offset="1" stop-color="#e4e2de"/></linearGradient>
      <linearGradient id="bootB" x1="0" y1="0" x2="0" y2="1"><stop offset="0" stop-color="#cfd0d0"/><stop offset="1" stop-color="#555"/></linearGradient>
      <linearGradient id="bootC" x1="0" y1="0" x2="0" y2="1"><stop offset="0" stop-color="#b0aaa0"/><stop offset="1" stop-color="#8a7a60"/></linearGradient>
    </defs>
    <polygon points="0,0 151,0 151,112 50,112" fill="url(#bootA)"/>
    <rect x="151" y="0" width="130" height="112" fill="url(#bootB)"/>
    <rect x="281" y="0" width="68" height="112" fill="url(#bootC)"/>
  </svg>
</section>
<svg class="ribbon" width="72" height="72" viewBox="0 0 72 72" aria-hidden="true"><polygon points="40,0 70,0 0,70 0,40" fill="var(--ribbon)"/><text x="30" y="32" transform="rotate(-45 30 32)" fill="#fff" font-family="Open Sans,sans-serif" font-size="8" font-weight="700" text-anchor="middle">FREE</text></svg>

<div class="footer-rule"></div>
<div class="footer-links"><a>Terms &amp; Conditions</a><a>About Us</a><a>Orders and Returns</a><a>Contact Us</a></div>
<div class="copyright">© 2012 Talvo Shoes. All Rights Reserved.</div>
<div class="pay" style="left:826px;width:30px;background:#3a5ea8"></div>
<div class="pay" style="left:862px;width:34px;background:#e4a838"></div>
<div class="pay" style="left:902px;width:50px;background:#c0c0c0"></div>
<div class="pay" style="left:958px;width:34px;background:#4a78c8"></div>
</body>
</html>
```